Double-Sided Tri-fold Brochure Needed for PTSD Service Dog Organization that serves US Veterans and

Our current brochure is in desperate need of a face lift. We want something fresh and are open to all ideas. We need our new logo added, we want to change some text around and add more information, and we want to update it with current photos. Text, I imagine, can be changed after winning design is selected. We use our brochure for fundraising, so we'd love to have it easy to read, yet able to make an emotional impact. We need to keep the donation mail-in form already on the old brochure. We are open to artist interpretations, however, for color scheme reference our website is: www.BlueMeadowCanineAllies.com

Target Market(s)

Veterans, First-Responders, Dog Lovers, Donors

Industry/Entity Type

It Service

Requirements
Must have
• Able to elicit an emotional response. We use our brochures for fundraising and information.
Should not have
• anything "cute"

```html
<!DOCTYPE html>
<html lang="en">
<head>
<meta charset="utf-8">
<title>Blue Meadow Canine Allies – Tri-fold Brochure</title>
<link href="https://fonts.googleapis.com/css2?family=Open+Sans:wght@400;600;700;800&display=swap" rel="stylesheet">
<style>
  :root{
    --green:#3e6b34;
    --green-dark:#2c4f25;
    --green-light:#6f9a5f;
    --ink:#2b2b2b;
    --muted:#6b6b6b;
    --paper:#ffffff;
    --backdrop:#ececec;
    --rule:#c9c9c9;
  }
  *{box-sizing:border-box;margin:0;padding:0}
  html,body{width:755px;height:1200px;overflow:hidden;background:var(--backdrop);font-family:"Open Sans",Arial,sans-serif;color:var(--ink)}
  .spread{position:absolute;left:27px;width:700px;height:541px;background:var(--paper);box-shadow:0 3px 10px rgba(0,0,0,.18);overflow:hidden;display:flex}
  .spread--outside{top:30px}
  .spread--inside{top:622px}
  .panel{position:relative;width:233.33px;height:100%;overflow:hidden}
  .panel + .panel{border-left:1px dashed #e2e2e2}
  .swoosh{position:absolute;left:0;width:100%}
  .photo{position:absolute}
  .photo--round{border-radius:50%;border:4px solid var(--paper);box-shadow:0 0 0 3px var(--green)}
  .h-green{color:var(--green);font-weight:800;font-size:15px}
  .h-white{color:#fff;font-weight:800;font-size:15px}
  .body{font-size:6.6px;line-height:1.5;color:var(--ink)}
  .body p{margin-bottom:6px}
  .body b{color:var(--green-dark)}
  .brand{display:flex;align-items:center;gap:6px}
  .brand__mark{width:22px;height:22px;background:var(--green);flex:none}
  .brand__name{font-weight:800;color:var(--green);font-size:10px;line-height:1.1;text-transform:uppercase}
  .web{font-size:7px;color:var(--green);font-weight:600}

  /* form panel */
  .form{position:absolute;left:18px;top:24px;right:18px}
  .form__title{font-size:9px;font-weight:700;color:var(--green);margin-bottom:10px}
  .form__row{font-size:6.5px;color:var(--muted);border-bottom:1px solid var(--rule);height:19px;display:flex;align-items:flex-end;padding-bottom:2px}
  .form__check{display:flex;gap:10px;font-size:6.5px;color:var(--muted);margin:10px 0 4px}
  .form__check span::before{content:"";display:inline-block;width:6px;height:6px;border:1px solid var(--muted);margin-right:3px;vertical-align:-1px}
  .mail-band{position:absolute;left:0;bottom:0;width:100%;height:112px;background:var(--green);color:#fff;padding:22px 18px;font-size:6.6px;line-height:1.6;text-align:center}

  /* contact panel */
  .contact{position:absolute;left:0;right:0;top:218px;text-align:center}
  .contact__item{display:flex;flex-direction:column;align-items:center;margin-top:10px;font-size:6.8px;line-height:1.45}
  .icon{width:16px;height:16px;border-radius:50%;background:var(--green);display:flex;align-items:center;justify-content:center;margin-bottom:3px}

  /* bullets */
  .reality-list{list-style:none;position:absolute;left:16px;right:14px;top:196px}
  .reality-list li{display:flex;gap:7px;align-items:flex-start;font-size:6.6px;line-height:1.45;margin-bottom:9px}
  .reality-list .icon{flex:none;margin:0}
</style>
</head>
<body>

<!-- OUTSIDE SPREAD -->
<section class="spread spread--outside">

  <div class="panel panel--form">
    <div class="form">
      <div class="form__title">Yes! I want to help a veteran heal.</div>
      <div class="form__row">Name</div>
      <div class="form__row">Address</div>
      <div class="form__row">City / State / Zip</div>
      <div class="form__row">Phone</div>
      <div class="form__row">Email</div>
      <div class="form__check"><span>$25</span><span>$50</span><span>$100</span><span>$250</span><span>Other</span></div>
      <div class="form__row">Amount enclosed $</div>
      <div class="form__row">In honor / memory of</div>
      <div class="form__row">Card number</div>
      <div class="form__row">Expiration / Signature</div>
    </div>
    <div class="mail-band">
      Please make checks payable to<br>
      <b>Blue Meadow Canine Allies</b><br>
      PO Box 4127<br>
      Cedar Hollow, TX 75001<br>
      Your gift is tax deductible to the full extent of the law.
    </div>
  </div>

  <div class="panel panel--contact">
    <svg class="swoosh" style="top:0" width="234" height="110" viewBox="0 0 234 110" preserveAspectRatio="none">
      <path d="M0 0H234V46C170 84 80 96 0 78Z" fill="var(--green)"/>
    </svg>
    <div class="photo photo--round" role="img" aria-label="Photo of a smiling handler with her service dog"
         style="left:22px;top:34px;width:118px;height:118px;background:linear-gradient(160deg,#c9b49a,#7a6a58 60%,#3b3a33)"></div>
    <div class="photo photo--round" role="img" aria-label="Photo of a black service dog"
         style="left:132px;top:96px;width:70px;height:70px;background:radial-gradient(circle at 45% 40%,#444,#141414)"></div>
    <div class="contact">
      <div class="h-green">Contact Us</div>
      <div class="contact__item">
        <span class="icon"><svg width="9" height="9" viewBox="0 0 24 24"><path d="M12 2a7 7 0 0 0-7 7c0 5 7 13 7 13s7-8 7-13a7 7 0 0 0-7-7zm0 9.5A2.5 2.5 0 1 1 12 6.5a2.5 2.5 0 0 1 0 5z" fill="#fff"/></svg></span>
        PO Box 4127<br>Cedar Hollow, TX 75001
      </div>
      <div class="contact__item">
        <span class="icon"><svg width="9" height="9" viewBox="0 0 24 24"><path d="M6.6 10.8a15 15 0 0 0 6.6 6.6l2.2-2.2a1 1 0 0 1 1-.25 11.4 11.4 0 0 0 3.6.6 1 1 0 0 1 1 1V20a1 1 0 0 1-1 1A17 17 0 0 1 3 4a1 1 0 0 1 1-1h3.5a1 1 0 0 1 1 1c0 1.25.2 2.45.6 3.6a1 1 0 0 1-.25 1z" fill="#fff"/></svg></span>
        (555) 014-2290
      </div>
      <div class="contact__item">
        <span class="icon"><svg width="9" height="9" viewBox="0 0 24 24"><path d="M3 6h18v12H3z" fill="none" stroke="#fff" stroke-width="2"/><path d="M3 6l9 7 9-7" fill="none" stroke="#fff" stroke-width="2"/></svg></span>
        hello@bluemeadowallies.org
      </div>
    </div>
    <div class="brand" style="position:absolute;left:56px;top:420px">
      <span class="brand__mark"></span>
      <span class="brand__name">Blue Meadow<br>Canine Allies</span>
    </div>
    <div class="web" style="position:absolute;left:0;right:0;top:470px;text-align:center">www.BlueMeadowCanineAllies.com</div>
    <svg class="swoosh" style="bottom:0" width="234" height="40" viewBox="0 0 234 40" preserveAspectRatio="none">
      <path d="M0 40V26C80 6 160 4 234 18V40Z" fill="var(--green)"/>
    </svg>
  </div>

  <div class="panel panel--cover">
    <svg class="swoosh" style="top:0" width="234" height="60" viewBox="0 0 234 60" preserveAspectRatio="none">
      <path d="M0 0H234V20C160 44 70 42 0 26Z" fill="var(--green)"/>
    </svg>
    <div class="brand" style="position:absolute;left:60px;top:58px">
      <span class="brand__mark" style="width:30px;height:30px"></span>
      <span class="brand__name" style="font-size:13px">Blue Meadow<br>Canine Allies</span>
    </div>
    <div class="photo" role="img" aria-label="Photo of a veteran's service dog" style="left:20px;top:118px;width:58px;height:46px;background:linear-gradient(#b08a5a,#5b4530)"></div>
    <div class="photo" role="img" aria-label="Photo of a golden retriever" style="left:88px;top:118px;width:58px;height:46px;background:linear-gradient(#d9b37a,#8c6838)"></div>
    <div class="photo" role="img" aria-label="Photo of a black labrador" style="left:156px;top:118px;width:58px;height:46px;background:linear-gradient(#555,#1c1c1c)"></div>
    <div class="photo photo--round" role="img" aria-label="Sunset silhouette of a veteran sitting with his service dog"
         style="left:34px;top:190px;width:166px;height:166px;background:radial-gradient(circle at 50% 60%,#f6d35c,#e88a2c 45%,#6b2f14 85%)"></div>
    <div class="body" style="position:absolute;left:22px;right:22px;top:378px;text-align:center;font-size:8px;font-weight:600;color:var(--green-dark)">
      Trained service dogs for veterans and first responders living with PTSD.
    </div>
    <div class="web" style="position:absolute;left:0;right:0;top:470px;text-align:center">www.BlueMeadowCanineAllies.com</div>
    <svg class="swoosh" style="bottom:0" width="234" height="40" viewBox="0 0 234 40" preserveAspectRatio="none">
      <path d="M0 40V18C80 4 160 6 234 26V40Z" fill="var(--green)"/>
    </svg>
  </div>
</section>

<!-- INSIDE SPREAD -->
<section class="spread spread--inside">

  <div class="panel panel--reality">
    <div class="photo" role="img" aria-label="Photo of a handler kneeling with a black service dog"
         style="left:0;top:0;width:100%;height:140px;background:linear-gradient(120deg,#6a5d4c,#2a2622 70%)"></div>
    <svg class="swoosh" style="top:112px" width="234" height="40" viewBox="0 0 234 40" preserveAspectRatio="none">
      <path d="M0 40V20C80 0 160 2 234 16V40Z" fill="var(--paper)"/>
      <path d="M0 22C80 2 160 4 234 18" fill="none" stroke="var(--green)" stroke-width="4"/>
    </svg>
    <div class="h-green" style="position:absolute;left:16px;top:160px">The Reality</div>
    <ul class="reality-list">
      <li><span class="icon"><svg width="8" height="8" viewBox="0 0 24 24"><path d="M4 12l5 5L20 6" fill="none" stroke="#fff" stroke-width="3"/></svg></span>Every day, many veterans lose their battle with post-traumatic stress long after returning home.</li>
      <li><span class="icon"><svg width="8" height="8" viewBox="0 0 24 24"><path d="M4 12l5 5L20 6" fill="none" stroke="#fff" stroke-width="3"/></svg></span>Wait lists for a trained service dog can stretch for years, and cost is a real barrier.</li>
      <li><span class="icon"><svg width="8" height="8" viewBox="0 0 24 24"><path d="M4 12l5 5L20 6" fill="none" stroke="#fff" stroke-width="3"/></svg></span>A dog at their side restores sleep, calm and the confidence to face the world again.</li>
    </ul>
    <div class="photo photo--round" role="img" aria-label="Photo of a golden retriever looking up"
         style="left:14px;top:378px;width:116px;height:116px;background:radial-gradient(circle at 45% 40%,#e2bd84,#9a7240)"></div>
    <div class="photo photo--round" role="img" aria-label="Photo of a black labrador in a service vest"
         style="left:128px;top:410px;width:82px;height:82px;background:radial-gradient(circle at 45% 40%,#4a4a4a,#111)"></div>
  </div>

  <div class="panel panel--mission">
    <div class="photo" role="img" aria-label="Photo of a black dog resting its head on a veteran's hand"
         style="left:0;top:0;width:100%;height:150px;background:linear-gradient(90deg,#3a3a3a,#101010)"></div>
    <div class="h-white" style="position:absolute;left:118px;top:16px">Our Mission</div>
    <div class="body" style="position:absolute;left:118px;right:12px;top:38px;color:#e8e8e8">
      We pair veterans and first responders with PTSD with fully trained service dogs, free of charge, so they can reclaim daily life.
    </div>
    <svg class="swoosh" style="top:126px" width="234" height="40" viewBox="0 0 234 40" preserveAspectRatio="none">
      <path d="M0 40V16C80 2 160 4 234 20V40Z" fill="var(--paper)"/>
      <path d="M0 18C80 4 160 6 234 22" fill="none" stroke="var(--green)" stroke-width="4"/>
    </svg>
    <div class="h-green" style="position:absolute;left:16px;top:176px">How Can You Help?</div>
    <div class="body" style="position:absolute;left:16px;right:16px;top:200px">
      <p>Every dog we place takes up to two years of training and care. Your support makes each match possible and keeps our program free to the heroes who need it most.</p>
      <p><b>Donate:</b> Use the mail-in form or give online.</p>
      <p><b>Sponsor a Dog:</b> Cover training for one future partner.</p>
      <p><b>Volunteer:</b> Help with puppy raising and events.</p>
      <p><b>Spread the Word:</b> Share our mission with your community.</p>
    </div>
    <svg class="swoosh" style="bottom:0" width="234" height="34" viewBox="0 0 234 34" preserveAspectRatio="none">
      <path d="M0 34V22C80 4 160 4 234 16V34Z" fill="var(--green)"/>
    </svg>
  </div>

  <div class="panel panel--services">
    <div class="h-green" style="position:absolute;left:16px;top:20px">Services We Offer</div>
    <div class="body" style="position:absolute;left:16px;right:16px;top:46px">
      <p>Blue Meadow Canine Allies provides service dogs trained to support people living with post-traumatic stress, traumatic brain injury and related conditions.</p>
      <p><b>PTSD Service Dogs:</b> Dogs trained to interrupt nightmares, ease anxiety, create space in crowds and guide their handler to a calm place.</p>
      <p><b>Handler Training:</b> Each veteran completes guided sessions with their dog to build a lasting, trusted working bond.</p>
      <p><b>Lifetime Support:</b> Our trainers stay in touch for the life of the team with follow-up visits and refresher classes.</p>
      <p><b>First Responder Program:</b> Police, fire and medical crews carry the same weight. We serve them with the same care.</p>
      <p><b>Community Outreach:</b> We speak with groups across the region about PTSD and the role of service dogs.</p>
    </div>
    <svg class="swoosh" style="bottom:0" width="234" height="40" viewBox="0 0 234 40" preserveAspectRatio="none">
      <path d="M0 40V16C80 2 160 6 234 24V40Z" fill="var(--green)"/>
    </svg>
  </div>
</section>

</body>
</html>
```